Flyer-Design für Datenschutzorganisation
Zielgruppe
Unsere Zielgruppe sind mittelständische Unternehmen ohne Ärzte und Apotheken, Mitarbeiterzahl 1-100 Personen, wir unterstützen Unternehmer und Unternehmen bei der Umsetzung der EU-Datenschutzgrundverordnung im Betrieb, wir sind ein VORTA-zertifiziertes Beratungsunternehmen
Aufgabenstellung
'Unsere vornehmliche Aufgabe liegt im Aufbau und der Umsetzung einer praxisnahen und gesetzeskonformen Datenschutzorganisation in Ihrem Unternehmen.'
'Nur wer alle Regeln kennt, kann sie auch einhalten'
'Egal, ob aus Ressourcengründen oder um den Blick eines externen Experten zu erhalten – unsere Beratung macht Sinn. Im Mittelpunkt steht dabei immer Ihr Unternehmen, Ihre Mitarbeiter und Ihre Projekte.'
'Wir sorgen für eine datenschutzkonforme Ausgestaltung der Prozesse in Ihrem Unternehmen im Umgang mit personenbezogenen Daten, ausgerichtet an der Zielsetzung Ihres Geschäftsmodells. Sie erhalten somit ein Rundum-sorglos-Paket im Datenschutz.'

```html
<!DOCTYPE html>
<html lang="de">
<head>
<meta charset="utf-8">
<title>Flyer Datenschutzorganisation – Velmar Consulting</title>
<link rel="stylesheet" href="https://fonts.googleapis.com/css2?family=Quicksand:wght@400;500;600&family=Oswald:wght@500&display=swap">
<style>
  :root {
    --bg: #d9d9d9;
    --paper: #ffffff;
    --navy: #141c4a;
    --navy-deep: #0c1640;
    --blue: #1f4f9c;
    --teal: #12a6c4;
    --ink: #3a3a3a;
    --brand: #1e3c8c;
    --band: rgba(190, 205, 240, 0.72);
  }
  * { box-sizing: border-box; margin: 0; padding: 0; }
  html, body { width: 1200px; height: 989px; overflow: hidden; }
  body {
    background: var(--bg);
    font-family: "Quicksand", sans-serif;
    color: var(--ink);
    position: relative;
  }
  .panel {
    position: absolute;
    width: 540px;
    height: 290px;
    overflow: hidden;
    box-shadow: 0 6px 18px rgba(0,0,0,0.18);
  }

  /* Rückseite: Kontakt */
  .panel--contact {
    left: 40px; top: 70px;
    background: var(--paper);
    padding: 24px 30px 0 30px;
  }
  .panel--contact .intro {
    font-size: 12.5px; line-height: 1.55; width: 430px;
  }
  .company { margin-top: 16px; font-size: 12.5px; line-height: 1.5; }
  .company__name { color: var(--blue); font-size: 15px; font-weight: 500; }
  .company__lead { font-size: 10.5px; }
  .badge {
    position: absolute; right: 34px; top: 38px;
    width: 36px; height: 36px; border: 2px solid var(--brand); border-radius: 50%;
  }
  .brand {
    position: absolute; right: 30px; bottom: 30px; text-align: right;
  }
  .brand__name {
    display: flex; align-items: center; gap: 8px; justify-content: flex-end;
    font-size: 20px; font-weight: 600; color: var(--brand);
  }
  .brand__mark { width: 14px; height: 14px; background: var(--brand); }
  .brand__web { font-size: 11px; margin-top: 4px; }
  .strip {
    position: absolute; left: 0; right: 0; bottom: 0; height: 8px; background: var(--navy);
  }

  /* Innenseite */
  .panel--inside { left: 40px; top: 420px; background: var(--paper); }
  .inside__visual {
    height: 170px;
    background:
      radial-gradient(ellipse 40% 70% at 72% 45%, rgba(150,190,230,0.55) 0%, rgba(150,190,230,0) 100%),
      linear-gradient(100deg, #0d2a5e 0%, #17437f 50%, #1a3566 100%);
  }
  .inside__text {
    padding: 18px 30px; font-size: 14px; line-height: 1.5;
  }

  /* Titel */
  .panel--cover {
    left: 620px; top: 245px; height: 340px;
    background: var(--navy-deep);
  }
  .cover__visual {
    position: absolute; inset: 0;
    background:
      radial-gradient(ellipse 32% 40% at 30% 62%, rgba(110,215,250,0.55) 0%, rgba(60,150,220,0.25) 55%, rgba(60,150,220,0) 100%),
      linear-gradient(155deg, var(--teal) 0%, #1b78b8 28%, var(--blue) 55%, var(--navy-deep) 100%);
  }
  .cover__headline {
    position: absolute; right: 0; top: 34px; z-index: 1;
    background: var(--band);
    border-radius: 14px 0 0 14px;
    padding: 14px 24px 14px 26px;
    font-family: "Oswald", sans-serif; font-weight: 500;
    color: #ffffff; text-transform: uppercase;
    font-size: 22px; line-height: 1.2; letter-spacing: 0.3px;
  }
</style>
</head>
<body>

  <section class="panel panel--contact">
    <p class="intro">Wir sorgen für eine datenschutzkonforme Ausgestaltung der Prozesse in Ihrem Unternehmen im Umgang mit personenbezogenen Daten, ausgerichtet an der Zielsetzung Ihres Geschäftsmodells. Sie erhalten somit ein Rundum-sorglos-Paket im Datenschutz.</p>
    <div class="company">
      <p class="company__name">Velmar Consulting GmbH</p>
      <p class="company__lead">Geschäftsführer: Markus Velmar</p>
      <p>Lindenweg 24</p>
      <p>82049 Pullach im Isartal</p>
      <p>Telefon +49 89 5550 1833</p>
      <p>Telefax +49 89 5550 1910</p>
      <p>kontakt@velmar-con.de</p>
    </div>
    <span class="badge" aria-hidden="true"></span>
    <div class="brand">
      <p class="brand__name"><span class="brand__mark"></span>Velmar</p>
      <p class="brand__web">www.velmar-con.de</p>
    </div>
    <span class="strip"></span>
  </section>

  <section class="panel panel--inside">
    <div class="inside__visual" role="img" aria-label="Foto: Hand berührt ein digitales Schloss in einem leuchtenden Netzwerk aus Punkten und Linien"></div>
    <p class="inside__text">Unsere vornehmliche Aufgabe liegt im Aufbau und der Umsetzung einer praxisnahen und gesetzeskonformen Datenschutzorganisation in Ihrem Unternehmen.</p>
    <span class="strip"></span>
  </section>

  <section class="panel panel--cover">
    <div class="cover__visual" role="img" aria-label="Illustration: leuchtendes Vorhängeschloss aus Netzlinien über einem aufgeklappten Laptop auf blauem Grund"></div>
    <h1 class="cover__headline">Nur wer alle Regeln kennt,<br>kann sie auch einhalten</h1>
  </section>

</body>
</html>
```